Business card for Eyelash extension salon in Larkmont Hills,California USA

We need new business card for our salon in Larkmont Hills. The salon name is 'Lumarra' . We would like to have...Business name: Lumarra Name of person: will provide later Address 6128 N.Corbel Ridge Blvd Larkmont Hills , CA 90299 Phone: will provide later (Text only) Web: www.lumarrastudio-example.com Pictogrid icon, Friendvale icon follow us for seasonal campaign and news @lumarrastudioexample Design should look elegant, high-end, clean, simple, cohesive with my brand. Please refer my brand board. Business name color will be metallic bronzy color. Im thinking grey background or white background. Thanks

Target Market(s)

25-35. Gender neutral. People who are in Entertainment business industry.
This is High-end Eyelash extension salon in Larkmont Hills

Industry/Entity Type

Beauty Salon

Contact Information for Business Card

Business name: Lumarra
Name of person: will provide later
Address 6128 N.Corbel Ridge Blvd Larkmont Hills , CA 90299
Phone: will provide later (Text only)
Web: www.lumarrastudio-example.com
Pictogrid icon, Friendvale icon
follow us for seasonal campaign and news @lumarrastudioexample

Requirements
Must have
• Beautiful, elegant, clean and simple look but very attractive and modern
Should not have
• We don't like too clutter, too busy designs.

```html
<!DOCTYPE html>
<html lang="en">
<head>
<meta charset="utf-8">
<title>Lumarra – Business Card</title>
<link rel="stylesheet" href="https://fonts.googleapis.com/css2?family=Crimson+Text:wght@400;600&family=Gloock&display=swap">
<style>
  :root {
    --stage: #1b1b1b;
    --card-white: #f7f7f7;
    --vein-light: #e4e4e4;
    --vein-mid: #cfcfcf;
    --panel: rgba(255, 255, 255, 0.82);
    --ink: #141414;
  }
  * { margin: 0; padding: 0; box-sizing: border-box; }
  html, body {
    width: 1200px;
    height: 741px;
    overflow: hidden;
    background: var(--stage);
  }
  .canvas {
    position: relative;
    width: 1200px;
    height: 741px;
    background: var(--stage);
  }
  .card {
    position: absolute;
    overflow: hidden;
    background: var(--card-white);
  }
  .card--front { left: 272px; top: 189px; width: 305px; height: 305px; }
  .card--back { left: 620px; top: 187px; width: 309px; height: 309px; }

  .card__marble {
    position: absolute;
    inset: 0;
    background:
      radial-gradient(ellipse at 12% 85%, var(--vein-mid) 0%, transparent 40%),
      radial-gradient(ellipse at 90% 20%, var(--vein-light) 0%, transparent 45%),
      radial-gradient(ellipse at 80% 90%, var(--vein-light) 0%, transparent 40%),
      linear-gradient(135deg, #fafafa 0%, #efefef 50%, #f8f8f8 100%);
  }
  .card__panel {
    position: absolute;
    left: 30px;
    top: 31px;
    width: 248px;
    height: 250px;
    border-radius: 25px;
    background: var(--panel);
  }
  .card__line {
    position: absolute;
    left: 0;
    width: 100%;
    text-align: center;
    color: var(--ink);
    font-family: "Crimson Text", serif;
    font-weight: 400;
    white-space: nowrap;
  }

  .brand-name {
    top: 104px;
    font-size: 46px;
    line-height: 56px;
    letter-spacing: 1px;
  }
  .web {
    font-size: 12.5px;
    line-height: 16px;
    font-weight: 600;
    letter-spacing: 0.9px;
  }
  .card--front .web { top: 195px; }
  .card--back .web { top: 198px; }

  .person-name {
    top: 49px;
    font-family: "Gloock", serif;
    font-size: 24px;
    line-height: 30px;
    letter-spacing: 0.3px;
  }
  .person-role { top: 86px; font-size: 12.5px; line-height: 15px; }
  .contact { font-size: 12.5px; line-height: 15px; }
  .contact b { font-weight: 600; }
  .contact--phone { top: 121px; }
  .contact--email { top: 136px; }
  .contact--street { top: 154px; }
  .contact--city { top: 169px; }
  .social-names {
    top: 227px;
    font-size: 10.5px;
    line-height: 13px;
    letter-spacing: 0.4px;
  }
  .handle { top: 243px; font-size: 12.5px; line-height: 15px; }
</style>
</head>
<body>
<main class="canvas">
  <section class="card card--front" aria-label="Card front">
    <div class="card__marble" role="img" aria-label="White and grey marble texture"></div>
    <div class="card__panel"></div>
    <p class="card__line brand-name">Lumarra</p>
    <p class="card__line web">www.lumarrastudio-example.com</p>
  </section>

  <section class="card card--back" aria-label="Card back">
    <div class="card__marble" role="img" aria-label="White and grey marble texture"></div>
    <div class="card__panel"></div>
    <h1 class="card__line person-name">Dara Whitlow</h1>
    <p class="card__line person-role">Owner</p>
    <p class="card__line contact contact--phone"><b>P:</b> +1 310 555 0148</p>
    <p class="card__line contact contact--email"><b>E:</b> info@studiomail-example.com</p>
    <p class="card__line contact contact--street">6128 N.Corbel Ridge Blvd Larkmont Hills</p>
    <p class="card__line contact contact--city">CA 90299</p>
    <p class="card__line web">www.lumarrastudio-example.com</p>
    <p class="card__line social-names">Friendvale · Pictogrid</p>
    <p class="card__line handle">@lumarrastudioexample</p>
  </section>
</main>
</body>
</html>
```